Web site for mobile& web developers

We need a web site design for our company, Marlow Fenwick Studio Pty Ltd.

We are a Sydney based, software development company specialising in mobile platforms and web applications. We are a small, dynamic team with a few awesome products we want to get out to the world.

We would prefer a clean, professional layout that incorporates the company logo and branding; we do have a youthful, start-up edge which we would like to express.

We technical people with damn good products, so your design has to make us look good to non-technical people too!

Target Market(s)

B2B, Enterprise technology, Project Managers, Marketing, Other developers

Industry/Entity Type

It Company

Requirements
Must have
• Required pages:
- home page - this must allow us to feature our software (mobile & web) on the home page
- a standard content page (for things like "about us", "our team", etc)
- contact us (including HTML form with error state)
- mobile (iOS and Android) product page - allow for screen shots, features, requirements, customer list
- web product page - allow for screen shots, features, requirements, customer list

You must incorporate our logo and branding into the theme.
Should not have
• HTML/CSS carve is not required. We only required layered PNGs or PSDs.

```html
<!DOCTYPE html>
<html lang="en">
<head>
<meta charset="utf-8">
<title>Marlow Fenwick Studio Pty Ltd</title>
<link href="https://fonts.googleapis.com/css2?family=Arimo:wght@400;700&display=swap" rel="stylesheet">
<style>
:root{
  --page:#ededed;
  --olive-top:#a9b80e;
  --olive-bottom:#7f8c05;
  --olive-text:#6b7a0a;
  --nav-text:#f4f6d8;
  --band:#6b6b6b;
  --panel-light:#e9e9e9;
  --panel-dark:#a9a9a9;
  --tab-border:#4e8a12;
  --body-text:#555;
  --green-soft:#e6f6c2;
  --green-btn:#7db61c;
  --footer:#666;
  --line:#cfd6c4;
}
*{margin:0;padding:0;box-sizing:border-box}
html,body{width:1200px;height:1078px;overflow:hidden;background:var(--page);font-family:"Arimo",Arial,sans-serif}
.site{position:relative;width:1200px;height:1078px}

.topbar{position:absolute;left:131px;top:0;width:938px;height:45px;background:linear-gradient(var(--olive-top),var(--olive-bottom));border-radius:0 0 4px 4px}
.topbar nav{position:absolute;left:17px;top:14px;font-size:12px;color:var(--nav-text);letter-spacing:.3px}
.topbar nav span.sep{margin:0 13px}
.subscribe{position:absolute;right:16px;top:8px;display:flex;gap:7px}
.subscribe .field{width:154px;height:27px;background:#f1f1f1;border:1px solid #cfcfcf;border-radius:3px;font-size:10px;color:#666;padding:8px 6px}
.subscribe .btn{width:62px;height:29px;background:linear-gradient(#eef2a4,#c5d24a);border:1px solid #7b860c;border-radius:4px;font-size:14px;color:#4e5605;text-align:center;line-height:27px}

.brand{position:absolute;left:171px;top:89px;display:flex;align-items:center}
.brand .mark{width:66px;height:66px;background:#78bd2a;border-radius:8px}
.brand-name{position:absolute;left:273px;top:93px;font-size:28px;color:var(--olive-text)}
.brand-tag{position:absolute;left:349px;top:132px;font-size:13px;color:#555}
.offices{position:absolute;left:715px;top:93px;width:350px}
.offices h2{font-weight:400;font-size:17px;color:var(--olive-text);text-align:center;margin-left:20px}
.offices ul{list-style:none;display:flex;gap:22px;margin-top:12px;font-size:14px;color:var(--olive-text)}
.offices li{display:flex;align-items:center;gap:12px}
.offices li i{display:block;width:14px;height:9px;background:#c8c8c8;border:1px solid #999}

.band{position:absolute;left:0;top:173px;width:1200px;height:349px;background:var(--band)}
.hero{position:absolute;left:134px;top:179px;width:932px;height:338px;border-radius:4px;background:linear-gradient(110deg,var(--panel-light) 25%,#bdbdbd 60%,#dcdcdc 100%);overflow:hidden}
.hero .phones{position:absolute;left:25px;top:60px;width:555px;height:270px;background:linear-gradient(#3a3a3a,#1c1c1c);border-radius:20px;opacity:.88}
.hero .bubbles{position:absolute;left:500px;top:60px;width:230px;height:275px;border-radius:50%;background:radial-gradient(circle,#4cb0e0 0%,#79c12a 60%,rgba(121,193,42,0) 72%)}
.hero h1{position:absolute;right:19px;top:25px;font-weight:400;font-size:14px;color:#fff}
.hero .tabs{position:absolute;left:670px;top:300px;display:flex;gap:17px}
.hero .tabs span{width:49px;height:26px;border:1px solid var(--tab-border);color:#111;font-size:14px;text-align:center;line-height:26px}

.content{position:absolute;left:136px;top:532px;width:652px;height:428px;background:#fff;border:1px solid #d0d0d0;border-radius:3px;overflow:hidden}
.side{position:absolute;left:0;top:0;width:168px;height:100%;background:linear-gradient(90deg,#e2e2e2,#fafafa 20%,#f4f4f4);border-right:2px solid #d8d8d8}
.side ul{list-style:none;margin-top:8px}
.side li{position:relative;height:32px;margin:0 18px 0 18px;border-bottom:1px solid #e4e4e4;font-size:12px;color:#444;padding:9px 0 0 19px}
.side li::before{content:"";position:absolute;left:1px;top:10px;width:10px;height:10px;border-radius:50%;background:#2a8bd0}
.side li.active{margin:0;padding-left:36px;background:linear-gradient(90deg,#c8e3f6,#eef6fc);border-bottom:0}
.side li.active::before{left:19px;background:#333}
.article{position:absolute;left:174px;top:14px;width:465px;font-size:12px;line-height:25.3px;color:var(--body-text);text-align:justify}
.article p+p{margin-top:0}
.article .gap{margin-top:25px}

.solutions{position:absolute;left:811px;top:534px;width:254px;height:227px;border:1px solid #cfd9b6;border-radius:4px;background:linear-gradient(#fff 20%,var(--green-soft));}
.solutions header{height:45px;border-bottom:1px solid #d3d3d3;background:#fff;border-radius:4px 4px 0 0;display:flex;align-items:center;padding-left:10px;gap:14px;font-size:13px;font-weight:700;color:#222}
.solutions header i{width:30px;height:26px;border-radius:50%;background:radial-gradient(#f3cf5e,#c1891b)}
.solutions ul{list-style:none;padding:0 6px 0 16px}
.solutions li{height:40.5px;border-bottom:1px solid var(--line);display:flex;align-items:center;gap:14px;font-size:12px;color:#555;padding-top:8px}
.solutions li svg{flex:none}

.casestudy{position:absolute;left:814px;top:778px;width:250px;height:182px;border:1px solid #cfcfcf;background:linear-gradient(#f8f8f8,#fff)}
.casestudy .device{position:absolute;left:58px;top:12px;width:150px;height:122px;border-radius:10px;background:linear-gradient(#2c2c2c,#0c0c0c)}
.casestudy .cta{position:absolute;left:0;bottom:0;width:100%;height:31px;background:linear-gradient(#9fd13a,#6aa617);color:#fff;font-weight:700;font-size:14px;text-align:center;line-height:31px}

.footer{position:absolute;left:133px;top:980px;width:933px;height:35px;background:var(--footer);border-radius:4px;color:#fff;font-size:12px}
.footer nav{position:absolute;left:11px;top:11px}
.footer nav span.sep{margin:0 9px}
.footer .copy{position:absolute;right:10px;top:11px}
</style>
</head>
<body>
<div class="site">

  <header class="topbar">
    <nav>Home<span class="sep">|</span>About Us<span class="sep">|</span>Our Products<span class="sep">|</span>Contact Us<span class="sep">|</span>Faq<span class="sep">|</span>Our Team<span class="sep">|</span>Help<span class="sep">|</span>Site Map</nav>
    <form class="subscribe">
      <div class="field">Email Addreass :</div>
      <div class="btn">Submit</div>
    </form>
  </header>

  <div class="brand"><span class="mark"></span></div>
  <div class="brand-name">Marlow Fenwick Studio Pty Ltd</div>
  <div class="brand-tag">Mobile Platforms And Web Applications</div>

  <div class="offices">
    <h2>Software Outsourcing Company</h2>
    <ul>
      <li><i></i>USA</li>
      <li><i></i>India</li>
      <li><i></i>Europe</li>
      <li><i></i>Canada</li>
    </ul>
  </div>

  <div class="band"></div>
  <section class="hero">
    <div class="phones" role="img" aria-label="Three smartphones showing a sports news mobile site"></div>
    <div class="bubbles" role="img" aria-label="Cluster of blue and green bubbles labelled with services: B2B, CRM, CMS, business directories, social network"></div>
    <h1>Marlow Fenwick Studio Pty Ltd</h1>
    <div class="tabs"><span>1</span><span>2</span><span>3</span><span>4</span></div>
  </section>

  <main class="content">
    <aside class="side">
      <ul>
        <li class="active">Software Development</li>
        <li>Web Applications</li>
        <li>Web Applications</li>
        <li>Mobile Development</li>
        <li>Cms Applications</li>
      </ul>
    </aside>
    <article class="article">
      <p>With offices in Dallas, Seattle and Victoria, Brightwell Software offers a unique combination of e-business strategy, creative web design and application expertise when developing website solutions for our clientele. We have applied a proven methodology that has helped us successfully deploy hundreds of commercial websites for organizations worldwide since 1993.</p>
      <p class="gap">Brightwell Software's eye-popping creative, strategic site architecture, and fluid usability design produces amazing results when integrated with web technology.</p>
      <p>We also provide complete end-to-end solutions such as Web CMS training, e-marketing services, social and mobile applications, and CMS hosting services.</p>
      <p class="gap">We also provide complete end-to-end solutions such as Web CMS training, e-marketing services, social and mobile applications.</p>
    </article>
  </main>

  <section class="solutions">
    <header><i></i>Best Business Solutions</header>
    <ul>
      <li><svg width="16" height="14" viewBox="0 0 16 14"><path d="M1 7l5 5L15 2" fill="none" stroke="#555" stroke-width="3"/></svg>Management Consulting</li>
      <li><svg width="16" height="14" viewBox="0 0 16 14"><path d="M1 7l5 5L15 2" fill="none" stroke="#555" stroke-width="3"/></svg>Management Consulting</li>
      <li><svg width="16" height="14" viewBox="0 0 16 14"><path d="M1 7l5 5L15 2" fill="none" stroke="#555" stroke-width="3"/></svg>Management Consulting</li>
      <li><svg width="16" height="14" viewBox="0 0 16 14"><path d="M1 7l5 5L15 2" fill="none" stroke="#555" stroke-width="3"/></svg>Management Consulting</li>
    </ul>
  </section>

  <section class="casestudy">
    <div class="device" role="img" aria-label="Tablet showing a video player"></div>
    <div class="cta">Watch a Video CMS Case Study</div>
  </section>

  <footer class="footer">
    <nav>Home<span class="sep">|</span>About Us<span class="sep">|</span>Our Products<span class="sep">|</span>Contact Us<span class="sep">|</span>Faq<span class="sep">|</span>Our Team<span class="sep">|</span>Help<span class="sep">|</span>Site Map</nav>
    <div class="copy">Copyright@Marlow Fenwick Studio Pty Ltd</div>
  </footer>

</div>
</body>
</html>
```